Boutique custom software development company needs new business card

Our nearly 20 year old custom software development company would like to better include the fact that we are now providing Bitcoin services. These new services are B2B include education (how to acquire and securely hold Bitcoin) and integrating Bitcoin payments into existing ecommerce sites or other existing systems. Please keep the card clean and simple. Attached is our current design and some other files. vexalon.example

Target Market(s)

businesses owners interested in long term relationship

Industry/Entity Type

Custom software development and Bitcoin

Contact Information for Business Card

Marcus Ellwood, marcus@vexalon.example, vexalon.example, (888) 555-VEXAL

Font styles to use
Other font styles liked:
• monospace

Requirements
Must have
• double-sided
Nice to have
• clean and simple
Should not have
• physical address

```html
<!DOCTYPE html>
<html lang="en">
<head>
<meta charset="utf-8">
<title>Vexalon Business Card</title>
<link rel="stylesheet" href="https://fonts.googleapis.com/css2?family=Red+Hat+Display:wght@400;500;700;800&family=Red+Hat+Mono:wght@500&display=swap">
<style>
  :root {
    --backdrop: #e4e4e4;
    --brand-blue: #376db3;
    --brand-blue-light: #93b6de;
    --brand-orange: #ea7a24;
    --card-white: #f4f4f4;
    --ink: #3a3a3a;
  }
  * { margin: 0; padding: 0; box-sizing: border-box; }
  html, body {
    width: 1200px;
    height: 960px;
    overflow: hidden;
  }
  body {
    position: relative;
    background: var(--backdrop);
    font-family: "Red Hat Display", Arial, sans-serif;
  }
  .card {
    position: absolute;
    left: 313px;
    width: 574px;
    height: 328px;
    overflow: hidden;
  }
  .card--front {
    top: 127px;
    background: var(--brand-blue);
    display: flex;
    align-items: center;
    justify-content: center;
  }
  .front-brand {
    display: flex;
    align-items: center;
    gap: 16px;
  }
  .front-brand__square {
    width: 44px;
    height: 44px;
    background: var(--brand-blue-light);
  }
  .front-brand__name {
    color: #ffffff;
    font-size: 46px;
    font-weight: 800;
    letter-spacing: 2px;
  }
  .card--back {
    top: 505px;
    background: var(--card-white);
  }
  .back-brand {
    position: absolute;
    left: 45px;
    top: 43px;
    writing-mode: vertical-rl;
    white-space: nowrap;
  }
  .back-brand__name {
    display: block;
    color: var(--brand-blue);
    font-size: 46px;
    font-weight: 800;
    line-height: 50px;
    letter-spacing: 0.5px;
  }
  .back-brand__tagline {
    display: block;
    margin-top: 8px;
    color: var(--brand-blue);
    font-size: 15px;
    font-weight: 500;
    line-height: 18px;
    letter-spacing: -0.2px;
  }
  .contact {
    position: absolute;
    left: 336px;
    top: 172px;
  }
  .contact__name {
    color: var(--brand-blue);
    font-size: 21px;
    font-weight: 700;
    letter-spacing: 0.6px;
    line-height: 26px;
    text-transform: uppercase;
  }
  .contact__services {
    margin: 4px 0 16px;
    color: var(--brand-orange);
    font-family: "Red Hat Mono", "Courier New", monospace;
    font-size: 10.5px;
    font-weight: 500;
    letter-spacing: 0.4px;
    line-height: 14px;
    text-transform: uppercase;
  }
  .contact__list { list-style: none; }
  .contact__item {
    display: flex;
    align-items: center;
    gap: 5px;
    color: var(--ink);
    font-size: 15px;
    line-height: 19.5px;
  }
  .contact__icon {
    width: 12px;
    height: 12px;
    flex: none;
  }
</style>
</head>
<body>
  <section class="card card--front">
    <div class="front-brand">
      <span class="front-brand__square"></span>
      <span class="front-brand__name">VEXALON</span>
    </div>
  </section>

  <section class="card card--back">
    <div class="back-brand">
      <span class="back-brand__name">VEXALON</span>
      <span class="back-brand__tagline">developer of custom applications</span>
    </div>

    <div class="contact">
      <p class="contact__name">Marcus Ellwood</p>
      <p class="contact__services">Custom software · Bitcoin services</p>
      <ul class="contact__list">
        <li class="contact__item">
          <svg class="contact__icon" viewBox="0 0 12 12" aria-hidden="true"><path d="M2.5 1 L4.5 1 L5.2 3.6 L3.9 4.6 Q4.9 6.9 7.4 8.1 L8.4 6.8 L11 7.5 L11 9.5 Q11 11 9.5 11 Q1 10.4 1 2.5 Q1 1 2.5 1 Z" fill="var(--brand-orange)"/></svg>
          <span>(888) 555-VEXAL</span>
        </li>
        <li class="contact__item">
          <svg class="contact__icon" viewBox="0 0 12 12" aria-hidden="true"><rect x="0.8" y="2.2" width="10.4" height="7.6" fill="none" stroke="var(--brand-orange)" stroke-width="1.4"/><path d="M1 2.6 L6 6.6 L11 2.6" fill="none" stroke="var(--brand-orange)" stroke-width="1.4"/></svg>
          <span>marcus@vexalon.example</span>
        </li>
        <li class="contact__item">
          <svg class="contact__icon" viewBox="0 0 12 12" aria-hidden="true"><g fill="none" stroke="var(--brand-orange)" stroke-width="1.1"><circle cx="6" cy="6" r="5"/><ellipse cx="6" cy="6" rx="2.2" ry="5"/><path d="M1 6 H11 M2 3.3 H10 M2 8.7 H10"/></g></svg>
          <span>vexalon.example</span>
        </li>
      </ul>
    </div>
  </section>
</body>
</html>
```